Design flat ui ios 7 inspired app

Know how you fit in the family and how you relate as a family through a shared Tree.
· Keep track of your family as it expands
· Merge family trees or join a common family Tree
· Share family moments by uploading pictures and videos on your calendar
· Get notifications of all events, additions, and other changes to the family tree
· Know where everyone is by keeping in touch through real-time chats
· Share your Tree with friends on social media
· Search for long lost family members and friends
· A great way for your kids to know where they come from

Providing a mobile app that allows users to not only create their family trees but allow them to invite other family members to participate in the completion of the family tree. • User downloads and installs the mobile app, then they proceed to signing up • Signing up the user should provide the following information; profile picture, first name, last name, date of birth, gender, password, email address, country, current city, mobile number • The next step is verifying the mobile number by asking the user to enter the six digit number that was sent to them via sms • Once the mobile number is verified your next step is to enter your family, start with you parents, then spouse(s) or partner(s), then siblings and children if any. This step should be optional, meaning users can skip this step • The app should have a menu bar at the bottom(action bar) with fiver menu items namely, Home, Edit, Tree, Stats, Calendar. • After the user has been signed in their first experience is the home screen, with the profile picture displayed, along with the user’s first name, last name, and age(all the above should be static). Just below all this are three tabs for notifications, photos, and birthdays. • The notifications tab will list all notifications one after the other in text form, example; Pete updated his high school, Bruno added a new member, Ursula has a graduation party coming up, Dmitri updated his work experience, Greta updated her maiden name, Hannah updated her siblings, Ernie updated his children etc. • Photo’s tab will list all pictures uploaded sorted by latest pictures uploaded and tagged in. One should be able to scroll through the pictures and then when they click on one they can slide though them one after the next viewing them. One should be able to go back to the home screen by clicking the back button. There should be an option to add more photos and share the current ones. • The last tab should be birthdays, which simply lists all birthdays of people who have been entered into the tree from parents to spouses to siblings to children. The birthdays should be listed sorted by month then day, and you should be able to see how old the person is turning. • The next menu bar is the Edit menu which has three tabs namely personal details, family and advanced details. Personal details will have the profile picture, first name, second name, last name, date of birth, gender, twin(if twin then state), relationship status(list spouse if not single), city or place of birth, and living or not. The next tab is the family tab which list and allows you to edit parents, spouse, siblings, and children. The last tab is advanced details, which is hobbies, languages, education, and work experience. • Then the most important part of the app is the Tree function which displays the users family tree, this is all the people added so far and each person is represented by a square with smooth edges, first name and last name displayed first, then age with a green button showing online and a red one showing offline, and below a profile picture. All the relations showed by a line joining the related people. If the person has many spouses they should be stacked together and kids don’t have to show which parent us theirs. One should be able to edit a profile, view a profile, view stats, invite and share. When you invite that person an sms should be generated and the user can enter the mobile number of the family member and once the family members accepts the invitation they then are a member of the tree who can receive notifications on any changes on the tree. Anyone should be able to invite anyone and everyone should see all notifications from everyone who is a member. • The next menu is the statistics menu which displays gender stats, age distribution, birthdays, relationship status, zodiac signs, living vs not living • The last one is the calendar menu which has a calendar where people can add events, upload media, and when a day is clicked and has events on, they should show at the bottom one after the other.

```html
<!DOCTYPE html>
<html lang="en">
<head>
<meta charset="utf-8">
<title>Rootline – Family Tree App Screens</title>
<link href="https://fonts.googleapis.com/css2?family=Open+Sans:wght@400;600;700&display=swap" rel="stylesheet">
<style>
  :root{
    --canvas:#29323a;
    --green:#7fd44a;
    --green-light:#99e05a;
    --green-text:#6cc63a;
    --dark-band:#3b3e3d;
    --white:#ffffff;
    --field:#f0f0f0;
    --field-line:#dcdcdc;
    --label:#454545;
    --muted:#8a8a8a;
    --divider:#ececec;
  }
  *{box-sizing:border-box;margin:0;padding:0}
  html,body{width:800px;height:1200px;overflow:hidden;background:var(--canvas)}
  body{font-family:"Open Sans",Arial,sans-serif}
  .board{position:absolute;left:0;top:0;width:933px;height:1400px;transform:scale(.85745);transform-origin:0 0}
  .screen{position:absolute;width:213px;overflow:hidden;background:var(--white)}
  .abs{position:absolute}

  .status{position:absolute;left:0;top:0;width:100%;height:16px;display:flex;justify-content:space-between;align-items:center;padding:0 6px;font-size:8px;color:var(--white);background:var(--green)}
  .status.clear{background:transparent}
  .status .battery{display:inline-block;width:16px;height:7px;border:1px solid #fff;border-radius:1px;vertical-align:middle;margin-left:3px;position:relative}
  .status .battery::after{content:"";position:absolute;left:1px;top:1px;width:3px;height:3px;background:#fff}
  .appbar{position:absolute;left:0;top:16px;width:100%;height:39px;background:var(--green);color:var(--white);display:flex;align-items:center;justify-content:center;font-size:12.5px;font-weight:600}
  .appbar .menu{position:absolute;left:11px;top:14px}
  .appbar .search{position:absolute;right:10px;top:13px}

  .photo{position:absolute;left:0;width:100%;height:98px;background:linear-gradient(135deg,#d9d9d9 0%,#f2f2f2 55%,#c9c9c9 100%)}
  .band{position:absolute;left:0;width:100%;height:42px;background:var(--dark-band)}
  .tabs{position:absolute;left:11px;width:191px;height:18px;border-radius:9px;background:var(--white);display:flex;overflow:hidden;font-size:8px;color:#555}
  .tabs span{flex:1;display:flex;align-items:center;justify-content:center}
  .tabs .on{background:var(--green);color:var(--white)}

  .label{position:absolute;font-size:7.5px;font-weight:700;color:var(--label);letter-spacing:.2px}
  .field{position:absolute;height:19px;border-radius:10px;background:var(--field);border:1px solid var(--field-line);font-size:7px;color:var(--muted);display:flex;align-items:center;padding-left:10px}
  .select::after{content:"";position:absolute;right:8px;top:7px;border-left:2.5px solid transparent;border-right:2.5px solid transparent;border-top:3px solid var(--green)}
  .btn{position:absolute;border-radius:14px;background:var(--green-light);color:#2f4a1c;font-size:10.5px;font-weight:600;display:flex;align-items:center;justify-content:center}

  .card{position:absolute;background:var(--white);border-radius:8px}
  .brand{position:absolute;left:0;width:100%;display:flex;flex-direction:column;align-items:center;gap:6px;font-size:15px;font-weight:700;color:var(--green)}
  .brand i{display:block;width:14px;height:14px;border-radius:50%;background:var(--green)}

  /* add family */
  .family-section{position:absolute;left:0;width:100%;height:188px;border-top:1px solid var(--divider)}
  .family-section h3{position:absolute;left:0;top:10px;width:100%;text-align:center;font-size:9.5px;font-weight:700;color:var(--green-text)}
  .family-section .plus{position:absolute;right:10px;top:8px;font-size:13px;color:var(--green);font-weight:600}
  .toggle{position:absolute;height:19px;border-radius:10px;border:1px solid var(--field-line);background:var(--field);overflow:hidden}
  .toggle .x{position:absolute;left:0;top:0;width:35px;height:100%;border-radius:10px;background:var(--green);color:#fff;font-size:9px;font-weight:700;display:flex;align-items:center;justify-content:center}
  .toggle .tick{position:absolute;right:6px;top:3px}
  .dots{position:absolute;left:0;width:100%;display:flex;justify-content:center;gap:5px}
  .dots i{width:8px;height:8px;border-radius:50%;background:#e8e8e8}
  .dots i:first-child{background:var(--green)}

  /* birthdays */
  .bday-row{position:absolute;left:0;width:100%;height:32px;border-top:1px solid var(--divider);font-size:7.5px;color:#666;display:flex;align-items:center}
  .bday-row .day{position:absolute;left:12px}
  .bday-row .box{position:absolute;left:24px;width:14px;height:14px;border:1px solid #ddd;background:#f5f5f5;font-size:6.5px;font-weight:700;color:#444;display:flex;align-items:center;justify-content:center}
  .bday-row .name{position:absolute;left:47px}
  .bday-row .age{position:absolute;left:118px}
  .pill{position:absolute;height:19px;border-radius:10px;background:#f0f0f0;border:1px solid #ddd;font-size:8px;font-weight:600;color:#555;display:flex;align-items:center;justify-content:center}
  .month-list{position:absolute;width:66px;text-align:center;font-size:7.5px;color:#666;line-height:17px}

  /* home */
  .note{position:absolute;left:0;width:100%;height:57px;background:var(--white);border-bottom:1px solid var(--divider)}
  .note.active{background:var(--green)}
  .note .avatar{position:absolute;left:9px;top:10px;width:36px;height:36px;border-radius:50%;background:linear-gradient(135deg,#cfcfcf,#8f8f8f)}
  .note .who{position:absolute;left:57px;top:9px;font-size:9px;font-weight:700;color:var(--green-text)}
  .note .what{position:absolute;left:57px;top:24px;font-size:7.5px;color:#777}
  .note .when{position:absolute;left:57px;top:38px;height:8px;padding:0 5px 0 11px;border-radius:4px;background:#eef7e6;font-size:5.5px;color:#777;display:flex;align-items:center}
  .note .when::before{content:"";position:absolute;left:2px;top:1px;width:6px;height:6px;border-radius:50%;background:var(--green)}
  .note.active .who,.note.active .what{color:#fff}
  .note.active .when{background:#fff}
  .note .go{position:absolute;right:10px;top:20px}
  .tabbar{position:absolute;left:0;width:100%;height:31px;background:#fff;display:flex}
  .tabbar div{flex:1;display:flex;flex-direction:column;align-items:center;justify-content:flex-end;padding-bottom:3px;gap:3px;font-size:6.5px;color:#666}
  .tabbar .on{color:var(--green)}
</style>
</head>
<body>
<main class="board">

  <!-- Splash -->
  <section class="screen splash" style="left:67px;top:61px;height:319px;background:none">
    <div class="abs" role="img" aria-label="Blurred family photo background" style="left:0;top:0;width:100%;height:100%;background:linear-gradient(160deg,#5d5a56 0%,#7a6e63 45%,#4d4c4a 100%)"></div>
    <div class="status clear"><span>●●●○○ NetCo</span><span>4:21PM</span><span>20%<i class="battery"></i></span></div>
    <div class="brand" style="top:70px;font-size:20px"><i style="width:20px;height:20px"></i>Rootline</div>
    <svg class="abs" style="left:84px;top:239px" width="44" height="44" viewBox="0 0 44 44">
      <circle cx="22" cy="22" r="18" fill="#2f3336" stroke="#ffffff" stroke-width="5"/>
      <circle cx="22" cy="22" r="18" fill="none" stroke="#7fd44a" stroke-width="5" stroke-dasharray="37.3 113.1" transform="rotate(-90 22 22)"/>
      <text x="22" y="25" text-anchor="middle" font-family="Open Sans, sans-serif" font-size="9" fill="#fff">33%</text>
    </svg>
  </section>

  <!-- Login -->
  <section class="screen login" style="left:325px;top:61px;height:372px;background:none">
    <div class="abs" role="img" aria-label="Blurred family photo background" style="left:0;top:0;width:100%;height:100%;background:linear-gradient(160deg,#5d5a56 0%,#7d736a 50%,#4f4d4b 100%)"></div>
    <div class="status clear"><span>●●●○○ NetCo</span><span>4:21PM</span><span>20%<i class="battery"></i></span></div>
    <div class="card" style="left:15px;top:30px;width:183px;height:327px">
      <div class="brand" style="top:40px"><i></i>Rootline</div>
      <div class="label" style="left:15px;top:119px">MOBILE NUMBER</div>
      <div class="field" style="left:15px;top:135px;width:153px"></div>
      <div class="label" style="left:15px;top:160px">PASSWORD</div>
      <div class="field" style="left:15px;top:175px;width:153px"></div>
      <div class="btn" style="left:15px;top:212px;width:153px;height:28px">LOGIN</div>
      <div class="abs" style="left:0;top:257px;width:100%;text-align:center;font-size:7.5px;color:#555">REGISTER</div>
      <div class="abs" style="left:55px;top:284px;width:73px;height:1px;background:#b8e99a"></div>
      <div class="abs" style="left:82px;top:275px;width:19px;height:19px;border-radius:50%;background:var(--green-light);color:#fff;font-size:7.5px;display:flex;align-items:center;justify-content:center">or</div>
      <div class="abs" style="left:0;top:299px;width:100%;text-align:center;font-size:7.5px;color:#555">FORGOT PASSWORD?</div>
    </div>
  </section>

  <!-- New Registration -->
  <section class="screen register" style="left:581px;top:61px;height:559px;background:var(--dark-band)">
    <div class="status"><span>●●●○○ NetCo</span><span>4:21PM</span><span>20%<i class="battery"></i></span></div>
    <header class="appbar" style="height:40px">
      <svg class="menu" width="12" height="10" viewBox="0 0 12 10"><path d="M0 1h12M0 5h12M0 9h12" stroke="#fff" stroke-width="1.5"/></svg>
      New Registration
      <svg class="search" width="12" height="12" viewBox="0 0 12 12"><circle cx="5" cy="5" r="3.8" fill="none" stroke="#fff" stroke-width="1.8"/><path d="M8 8l3.3 3.3" stroke="#fff" stroke-width="2"/></svg>
    </header>
    <form class="card" style="left:16px;top:72px;width:182px;height:471px">
      <div class="label" style="left:13px;top:10px">PROFILE PICTURE</div>
      <div class="field" style="left:13px;top:22px;width:153px"></div>
      <div class="btn" style="left:114px;top:22px;width:52px;height:19px;font-size:7px;color:#fff;background:var(--green)">BROWS</div>

      <div class="label" style="left:13px;top:51px">FIRST NAME</div>
      <div class="field" style="left:13px;top:63px;width:153px">PETE</div>

      <div class="label" style="left:13px;top:92px">LAST NAME</div>
      <div class="field" style="left:13px;top:104px;width:153px">SMITH</div>

      <div class="label" style="left:13px;top:132px">DATE OF BIRTH</div>
      <div class="field select" style="left:13px;top:144px;width:36px">1</div>
      <div class="field select" style="left:58px;top:144px;width:46px">JAN</div>
      <div class="field select" style="left:111px;top:144px;width:55px">1985</div>

      <div class="label" style="left:13px;top:173px">GENDER</div>
      <div class="field select" style="left:13px;top:185px;width:153px">MALE</div>

      <div class="label" style="left:13px;top:214px">PASSWORD</div>
      <div class="field" style="left:13px;top:226px;width:153px">**********</div>

      <div class="label" style="left:13px;top:254px">EMAIL ADDRESS</div>
      <div class="field" style="left:13px;top:266px;width:153px">AB@EXAMPLE.COM</div>

      <div class="label" style="left:13px;top:295px">COUNTRY</div>
      <div class="field select" style="left:13px;top:307px;width:153px">INDIA</div>

      <div class="label" style="left:13px;top:336px">CURRENT CITY</div>
      <div class="field" style="left:13px;top:348px;width:153px">NEW DELHI</div>

      <div class="label" style="left:13px;top:376px">MOBILE NUMBER</div>
      <div class="field" style="left:13px;top:388px;width:153px">+91-900123XXXX</div>

      <div class="btn" style="left:13px;top:426px;width:153px;height:28px">REGISTER NOW</div>
    </form>
  </section>

  <!-- Add Family -->
  <section class="screen add-family" style="left:67px;top:418px;height:850px">
    <div class="status"><span>●●●○○ NetCo</span><span>4:21PM</span><span>20%<i class="battery"></i></span></div>
    <header class="appbar" style="height:38px">
      <svg class="menu" width="12" height="10" viewBox="0 0 12 10"><path d="M0 1h12M0 5h12M0 9h12" stroke="#fff" stroke-width="1.5"/></svg>
      Add Family
      <svg class="search" width="12" height="12" viewBox="0 0 12 12"><circle cx="5" cy="5" r="3.8" fill="none" stroke="#fff" stroke-width="1.8"/><path d="M8 8l3.3 3.3" stroke="#fff" stroke-width="2"/></svg>
    </header>
    <div class="band" style="top:54px;height:44px">
      <div class="tabs" style="top:12px;height:19px"><span></span><span class="on">Family</span><span></span></div>
    </div>

    <div class="family-section" style="top:98px;border-top:none">
      <h3>PARENTS</h3><span class="plus">+</span>
      <div class="field" style="left:11px;top:28px;width:191px"></div>
      <div class="field" style="left:11px;top:53px;width:191px"></div>
      <div class="label" style="left:11px;top:78px">DATE OF BIRTH</div>
      <div class="field select" style="left:11px;top:94px;width:46px">1</div>
      <div class="field select" style="left:63px;top:94px;width:59px">JAN</div>
      <div class="field select" style="left:127px;top:94px;width:75px">1985</div>
      <div class="label" style="left:11px;top:117px">GENDER</div>
      <div class="label" style="left:138px;top:117px">ALIVE</div>
      <div class="field select" style="left:11px;top:133px;width:120px">MALE</div>
      <div class="toggle" style="left:138px;top:133px;width:64px"><span class="x">X</span><svg class="tick" width="10" height="10" viewBox="0 0 10 10"><path d="M1 5l3 3 5-6" fill="none" stroke="#888" stroke-width="1.4"/></svg></div>
      <div class="dots" style="top:164px"><i></i><i></i><i></i></div>
    </div>

    <div class="family-section" style="top:287px">
      <h3>SPOUSES</h3><span class="plus">+</span>
      <div class="field" style="left:11px;top:28px;width:191px"></div>
      <div class="field" style="left:11px;top:53px;width:191px"></div>
      <div class="label" style="left:11px;top:78px">DATE OF BIRTH</div>
      <div class="field select" style="left:11px;top:94px;width:46px">1</div>
      <div class="field select" style="left:63px;top:94px;width:59px">JAN</div>
      <div class="field select" style="left:127px;top:94px;width:75px">1985</div>
      <div class="label" style="left:11px;top:117px">GENDER</div>
      <div class="label" style="left:138px;top:117px">ALIVE</div>
      <div class="field select" style="left:11px;top:133px;width:120px">MALE</div>
      <div class="toggle" style="left:138px;top:133px;width:64px"><span class="x">X</span><svg class="tick" width="10" height="10" viewBox="0 0 10 10"><path d="M1 5l3 3 5-6" fill="none" stroke="#888" stroke-width="1.4"/></svg></div>
      <div class="dots" style="top:164px"><i></i><i></i><i></i></div>
    </div>

    <div class="family-section" style="top:475px">
      <h3>SHIBLINGS</h3><span class="plus">+</span>
      <div class="field" style="left:11px;top:28px;width:191px"></div>
      <div class="field" style="left:11px;top:53px;width:191px"></div>
      <div class="label" style="left:11px;top:78px">DATE OF BIRTH</div>
      <div class="field select" style="left:11px;top:94px;width:46px">1</div>
      <div class="field select" style="left:63px;top:94px;width:59px">JAN</div>
      <div class="field select" style="left:127px;top:94px;width:75px">1985</div>
      <div class="label" style="left:11px;top:117px">GENDER</div>
      <div class="label" style="left:138px;top:117px">ALIVE</div>
      <div class="field select" style="left:11px;top:133px;width:120px">MALE</div>
      <div class="toggle" style="left:138px;top:133px;width:64px"><span class="x">X</span><svg class="tick" width="10" height="10" viewBox="0 0 10 10"><path d="M1 5l3 3 5-6" fill="none" stroke="#888" stroke-width="1.4"/></svg></div>
      <div class="dots" style="top:164px"><i></i><i></i><i></i></div>
    </div>

    <div class="family-section" style="top:662px">
      <h3>CHILDREN</h3><span class="plus">+</span>
      <div class="field" style="left:11px;top:28px;width:191px"></div>
      <div class="field" style="left:11px;top:53px;width:191px"></div>
      <div class="label" style="left:11px;top:78px">DATE OF BIRTH</div>
      <div class="field select" style="left:11px;top:94px;width:46px">1</div>
      <div class="field select" style="left:63px;top:94px;width:59px">JAN</div>
      <div class="field select" style="left:127px;top:94px;width:75px">1985</div>
      <div class="label" style="left:11px;top:117px">GENDER</div>
      <div class="label" style="left:138px;top:117px">ALIVE</div>
      <div class="field select" style="left:11px;top:133px;width:120px">MALE</div>
      <div class="toggle" style="left:138px;top:133px;width:64px"><span class="x">X</span><svg class="tick" width="10" height="10" viewBox="0 0 10 10"><path d="M1 5l3 3 5-6" fill="none" stroke="#888" stroke-width="1.4"/></svg></div>
      <div class="dots" style="top:164px"><i></i><i></i><i></i></div>
    </div>
  </section>

  <!-- Profile: birthdays by month -->
  <section class="screen profile-month" style="left:325px;top:472px;height:338px">
    <div class="status"><span>●●●○○ NetCo</span><span>4:21PM</span><span>20%<i class="battery"></i></span></div>
    <header class="appbar">
      <svg class="menu" width="12" height="10" viewBox="0 0 12 10"><path d="M0 1h12M0 5h12M0 9h12" stroke="#fff" stroke-width="1.5"/></svg>
      Pete Smith
      <svg class="search" width="12" height="12" viewBox="0 0 12 12"><circle cx="5" cy="5" r="3.8" fill="none" stroke="#fff" stroke-width="1.8"/><path d="M8 8l3.3 3.3" stroke="#fff" stroke-width="2"/></svg>
    </header>
    <div class="photo" style="top:55px" role="img" aria-label="Profile photo of Pete Smith"></div>
    <div class="band" style="top:153px">
      <div class="tabs" style="top:12px"><span>Notifications</span><span>Photos</span><span class="on">Birthdays</span></div>
    </div>
    <svg class="abs" style="left:10px;top:211px" width="8" height="11" viewBox="0 0 8 11"><path d="M7 1L2 5.5 7 10" fill="none" stroke="#7fd44a" stroke-width="1.8"/></svg>
    <div class="pill" style="left:28px;top:207px;width:60px;height:18px">January</div>
    <div class="bday-row" style="top:240px"><span class="day">9</span><span class="box">8</span><span class="name">Pete Doe</span><span class="age">31 Years</span></div>
    <div class="bday-row" style="top:274px"><span class="day">18</span><span class="box"></span><span class="name">Pete Doe</span><span class="age">31 Years</span></div>
    <div class="bday-row" style="top:306px"><span class="day">31</span><span class="box"></span><span class="name">Pete Doe</span><span class="age">31 Years</span></div>
  </section>

  <!-- Profile: birthdays overview -->
  <section class="screen profile-year" style="left:325px;top:843px;height:373px">
    <div class="status"><span>●●●○○ NetCo</span><span>4:21PM</span><span>20%<i class="battery"></i></span></div>
    <header class="appbar" style="height:38px">
      <svg class="menu" width="12" height="10" viewBox="0 0 12 10"><path d="M0 1h12M0 5h12M0 9h12" stroke="#fff" stroke-width="1.5"/></svg>
      Pete Smith
      <svg class="search" width="12" height="12" viewBox="0 0 12 12"><circle cx="5" cy="5" r="3.8" fill="none" stroke="#fff" stroke-width="1.8"/><path d="M8 8l3.3 3.3" stroke="#fff" stroke-width="2"/></svg>
    </header>
    <div class="photo" style="top:54px" role="img" aria-label="Profile photo of Pete Smith"></div>
    <div class="band" style="top:152px">
      <div class="tabs" style="top:12px"><span>Notifications</span><span>Photos</span><span class="on">Birthdays</span></div>
    </div>
    <div class="pill" style="left:11px;top:207px;width:57px">January</div>
    <div class="pill" style="left:77px;top:207px;width:58px">February</div>
    <div class="pill" style="left:143px;top:207px;width:59px">March</div>
    <div class="month-list" style="left:7px;top:230px">9 Pete Doe<br>18 Jane Doe<br>21 Joe Doe</div>
    <div class="month-list" style="left:73px;top:230px">27 Jude Doe<br>27 Jude Doe<br>27 Jude Doe</div>
    <div class="pill" style="left:11px;top:292px;width:57px">April</div>
    <div class="pill" style="left:77px;top:292px;width:58px">May</div>
    <div class="pill" style="left:143px;top:292px;width:59px">June</div>
    <div class="month-list" style="left:7px;top:315px">11 Jeff Doe<br>21 Pete Doe<br>25 Greta Deo</div>
    <div class="month-list" style="left:73px;top:315px">21 Jude Doe<br>27 Jude Doe<br>31 Jude Doe</div>
  </section>

  <!-- Home: notifications -->
  <section class="screen home" style="left:581px;top:629px;height:399px;background:var(--dark-band)">
    <div class="status"><span>●●●○○ NetCo</span><span>4:21PM</span><span>20%<i class="battery"></i></span></div>
    <header class="appbar" style="height:38px">
      <svg class="menu" width="12" height="10" viewBox="0 0 12 10"><path d="M0 1h12M0 5h12M0 9h12" stroke="#fff" stroke-width="1.5"/></svg>
      Pete Smith
      <svg class="search" width="12" height="12" viewBox="0 0 12 12"><circle cx="5" cy="5" r="3.8" fill="none" stroke="#fff" stroke-width="1.8"/><path d="M8 8l3.3 3.3" stroke="#fff" stroke-width="2"/></svg>
    </header>
    <div class="abs" style="left:0;top:54px;width:100%;height:57px;background:var(--green)"></div>
    <div class="abs" role="img" aria-label="Round profile photo of Pete Smith" style="left:57px;top:54px;width:100px;height:100px;border-radius:50%;border:3px solid #fff;background:linear-gradient(135deg,#e4e4e4,#a9a9a9)"></div>
    <svg class="abs" style="left:133px;top:129px" width="20" height="20" viewBox="0 0 20 20"><circle cx="10" cy="10" r="9.5" fill="#7fd44a"/><circle cx="9" cy="9" r="3" fill="none" stroke="#fff" stroke-width="1.5"/><path d="M11.2 11.2l3 3" stroke="#fff" stroke-width="1.6"/></svg>
    <div class="tabs" style="left:12px;top:165px;width:190px"><span class="on">Notifications</span><span>Photos</span><span>Birthdays</span></div>

    <div class="note" style="top:196px">
      <div class="avatar" role="img" aria-label="Profile photo of Pete Smith"></div>
      <div class="who">Pete Smith</div><div class="what">Update his high school</div><div class="when">10 mints</div>
      <svg class="go" width="18" height="18" viewBox="0 0 18 18"><circle cx="9" cy="9" r="8" fill="none" stroke="#7fd44a" stroke-width="1.5"/><path d="M7.5 5.5L11 9l-3.5 3.5" fill="none" stroke="#7fd44a" stroke-width="1.6"/></svg>
    </div>
    <div class="note active" style="top:253px">
      <div class="avatar" role="img" aria-label="Profile photo of Pete Smith"></div>
      <div class="who">Pete Smith</div><div class="what">Update his high school</div><div class="when">10 mints</div>
      <svg class="go" width="18" height="18" viewBox="0 0 18 18"><circle cx="9" cy="9" r="8" fill="none" stroke="#fff" stroke-width="1.5"/><path d="M7.5 5.5L11 9l-3.5 3.5" fill="none" stroke="#fff" stroke-width="1.6"/></svg>
    </div>
    <div class="note" style="top:310px">
      <div class="avatar" role="img" aria-label="Profile photo of Pete Smith"></div>
      <div class="who">Pete Smith</div><div class="what">Update his high school</div><div class="when">10 mints</div>
      <svg class="go" width="18" height="18" viewBox="0 0 18 18"><circle cx="9" cy="9" r="8" fill="none" stroke="#7fd44a" stroke-width="1.5"/><path d="M7.5 5.5L11 9l-3.5 3.5" fill="none" stroke="#7fd44a" stroke-width="1.6"/></svg>
    </div>

    <nav class="tabbar" style="top:368px">
      <div class="on"><svg width="10" height="9" viewBox="0 0 10 9"><path d="M5 0L0 4.5h1.5V9h2.5V6h2v3h2.5V4.5H10z" fill="#7fd44a"/></svg>HOME</div>
      <div><svg width="9" height="9" viewBox="0 0 9 9"><path d="M1 8l1.5-3.5L7 0l2 2-4.5 4.5z" fill="#777"/></svg>EDIT</div>
      <div><svg width="9" height="9" viewBox="0 0 9 9"><circle cx="4.5" cy="3" r="2.5" fill="none" stroke="#777"/><path d="M4.5 5.5V9" stroke="#777"/></svg>TREE</div>
      <div><svg width="9" height="9" viewBox="0 0 9 9"><rect x=".5" y="1.5" width="8" height="7" fill="none" stroke="#777"/><path d="M.5 3.5h8" stroke="#777"/></svg>CALENDER</div>
      <div><svg width="10" height="9" viewBox="0 0 10 9"><path d="M1 9V5h2v4zM4 9V1h2v8zM7 9V3h2v6z" fill="#777"/></svg>STATS</div>
    </nav>
  </section>

</main>
</body>
</html>
```